We want to design total new business card and logo for Kestrel Building Services Ltd

Our company name Kestrel Building Services Ltd. Design new logo and business card , need hi-end luxury style art for architecture and construction industry. The card should simple but stylish. Our business focus on CONNECT tradesman to construction company, help marketing construction company tender oversea projects, managing franchise in construction sector, delivery amazing services to our client, so Logo should show the CONNECTION IDEA, CONNECTING PEOPLE, LUXURY. Visit our website for more information: kestrelhub.co.nz

Low design quality

Target Market(s)

Directors or managers

Industry/Entity Type

Construction Company

Contact Information for Business Card

Name, Title, Mobile, Email, Website

Font styles to use
Serif

Colors

Designer to choose colors to be used in the design.

Requirements
Must have
• Simple and luxury, connection icon
Nice to have
• Special materials, plastic card, look through,...
• Look new ideas.

```html
<!DOCTYPE html>
<html lang="en">
<head>
<meta charset="utf-8">
<title>Kestrel Building Services – Business Card</title>
<link rel="stylesheet" href="https://fonts.googleapis.com/css2?family=Tinos:wght@400;700&family=Poppins:wght@400;500;600&display=swap">
<style>
  :root {
    --page-bg: #e9ebed;
    --card-white: #ffffff;
    --brand-blue: #2ab3cf;
    --brand-blue-deep: #1596b4;
    --ink: #1d1d1f;
    --ink-soft: #3a3a3c;
    --card-shadow: 0 18px 40px rgba(0, 0, 0, 0.18);
  }
  * { box-sizing: border-box; margin: 0; padding: 0; }
  html, body {
    width: 1200px;
    height: 900px;
    overflow: hidden;
    background: var(--page-bg);
  }
  .canvas {
    position: relative;
    width: 1200px;
    height: 900px;
  }
  .card {
    position: absolute;
    width: 620px;
    height: 354px;
    border-radius: 4px;
    box-shadow: var(--card-shadow);
    overflow: hidden;
  }

  /* Back of card */
  .card-back {
    left: 80px;
    top: 80px;
    background: linear-gradient(135deg, var(--brand-blue) 0%, var(--brand-blue-deep) 100%);
    display: flex;
    align-items: center;
    justify-content: center;
  }
  .card-back .brand-name {
    font-family: "Tinos", serif;
    font-weight: 700;
    font-size: 34px;
    letter-spacing: 2px;
    color: var(--card-white);
    text-transform: uppercase;
  }

  /* Front of card */
  .card-front {
    left: 500px;
    top: 440px;
    background: var(--card-white);
  }
  .brand-lockup {
    position: absolute;
    top: 52px;
    left: 0;
    right: 0;
    text-align: center;
  }
  .brand-lockup .brand-row {
    display: inline-flex;
    align-items: center;
    gap: 12px;
  }
  .brand-mark-square {
    width: 22px;
    height: 22px;
    background: var(--brand-blue);
  }
  .brand-lockup .brand-name {
    font-family: "Tinos", serif;
    font-weight: 700;
    font-size: 30px;
    letter-spacing: 1px;
    color: var(--ink);
    text-transform: uppercase;
  }
  .brand-lockup .tagline {
    margin-top: 4px;
    font-family: "Tinos", serif;
    font-weight: 700;
    font-size: 15px;
    color: var(--brand-blue);
  }

  .person {
    position: absolute;
    left: 58px;
    top: 172px;
    width: 220px;
    text-align: right;
    font-family: "Poppins", sans-serif;
  }
  .person .person-name {
    font-size: 26px;
    font-weight: 600;
    color: var(--brand-blue);
    line-height: 1.15;
  }
  .person .person-title {
    font-size: 17px;
    font-weight: 400;
    color: var(--ink-soft);
  }

  .divider {
    position: absolute;
    left: 300px;
    top: 160px;
    width: 2px;
    height: 90px;
    background: var(--ink-soft);
  }

  .contacts {
    position: absolute;
    left: 324px;
    top: 158px;
    list-style: none;
    font-family: "Poppins", sans-serif;
    font-size: 17px;
    font-weight: 500;
    color: var(--ink);
  }
  .contacts li {
    display: flex;
    align-items: center;
    gap: 10px;
    height: 30px;
  }
  .contacts svg {
    width: 18px;
    height: 18px;
    flex: none;
    fill: var(--brand-blue);
  }

  .website {
    position: absolute;
    right: 40px;
    top: 282px;
    font-family: "Poppins", sans-serif;
    font-size: 17px;
    font-weight: 500;
    color: var(--ink);
  }
  .bottom-band {
    position: absolute;
    left: 0;
    right: 0;
    bottom: 0;
    height: 16px;
    background: var(--brand-blue);
  }
</style>
</head>
<body>
<main class="canvas">

  <section class="card card-back" aria-label="Business card back">
    <span class="brand-name">Kestrel</span>
  </section>

  <section class="card card-front" aria-label="Business card front">
    <header class="brand-lockup">
      <div class="brand-row">
        <span class="brand-mark-square"></span>
        <span class="brand-name">Kestrel Building Services</span>
      </div>
      <p class="tagline">Solid craft Honest value always</p>
    </header>

    <div class="person">
      <p class="person-name">YOUR NAME</p>
      <p class="person-title">Your Title</p>
    </div>

    <div class="divider"></div>

    <ul class="contacts">
      <li>
        <svg viewBox="0 0 24 24" aria-hidden="true"><path d="M6.6 10.8a15.1 15.1 0 0 0 6.6 6.6l2.2-2.2a1 1 0 0 1 1-.25 11.4 11.4 0 0 0 3.6.57 1 1 0 0 1 1 1V20a1 1 0 0 1-1 1A17 17 0 0 1 3 4a1 1 0 0 1 1-1h3.5a1 1 0 0 1 1 1c0 1.25.2 2.45.57 3.6a1 1 0 0 1-.25 1z"/></svg>
        <span>0800 417 352</span>
      </li>
      <li>
        <svg viewBox="0 0 24 24" aria-hidden="true"><path d="M6.6 10.8a15.1 15.1 0 0 0 6.6 6.6l2.2-2.2a1 1 0 0 1 1-.25 11.4 11.4 0 0 0 3.6.57 1 1 0 0 1 1 1V20a1 1 0 0 1-1 1A17 17 0 0 1 3 4a1 1 0 0 1 1-1h3.5a1 1 0 0 1 1 1c0 1.25.2 2.45.57 3.6a1 1 0 0 1-.25 1z"/></svg>
        <span>021 538 9071</span>
      </li>
      <li>
        <svg viewBox="0 0 24 24" aria-hidden="true"><path d="M2 5h20v14H2z M3.5 6.5 12 13l8.5-6.5" fill="var(--brand-blue)" stroke="#fff" stroke-width="1.5"/></svg>
        <span>info@kestrelhub.co.nz</span>
      </li>
    </ul>

    <p class="website">www.kestrelhub.co.nz</p>

    <div class="bottom-band"></div>
  </section>

</main>
</body>
</html>
```